Orlyn - Adventurous, Fun, Exciting, Social Fitness Club needs a Biz Card/Promo Card with Attitude!

Orlyn... we're a fun, social, outdoor fitness club that needs not just a Business Card for our Trainers, but a mini-promo card that shows off our unique, innovative and cheeky personality/brand to the world!
Who Are We? We're a fun & social fitness club that prides ourselves on getting our members outdoors trying new, exciting physical activities in an effort to find joy in an active lifestyle, and sharing that experience with other like minded people. We offer:
- Personal Training (1-on-1 Fitness Training)
- Group Fitness Classes (Boxing, Pilates, etc)
- Boot Camps (Military Style - Sandbags, Ropes, Tyres, etc)
- Events (Fun Runs, Triathlons, Ocean Swims, Treks, etc)
- Adventures (Machu Picchu Trek, Rock Climbing, Kayaking, etc)
Our tag line is 'No Judgements. No Limits!' The business card should be bold, exciting, adventurous and innovative, illustrating the values of our brand: possibility, thirst for life, personal accomplishment & freedom. It should be fun, friendly & inviting... but not over the top. Think trendy surf brand style of look.
Forget your standard, boring, basic business cards that are just for contact details, our business card actually has 4 key purposes:
(1) Provide our contact details
(2) Highlight main benefits of what we do
(3) Lead generation via the offer of a Free Trial
(4) Direct people to "Like" us on Chatterloop
(see an example of business card/promo card combo attached)
THE DESIGN MUST COMPLIMENT & BE CONSISTENT IN LOOK WITH OUR NEWLY DESIGNED WEBSITE (see attached)
Look forward to seeing what you come up with! ;)

Industry/Entity Type
Fitness
Requirements
Must have
- - Please see attached Layout for all requirements
- Primary Colour to be orange + some limited use of darker orange shading (as per website)
- Want to see white dotted patten, dark orange "splat" (as per website).
Nice to have
- - size preference is 90 x 45mm.
Should not have
- - No rounded edges
- Only very minimal/no use of the "sun rays" effect (as used behind logo in the website design)

```html
<!DOCTYPE html>
<html lang="en">
<head>
<meta charset="utf-8">
<title>Orlyn Fitness Clubs – Business &amp; Promo Card</title>
<link rel="stylesheet" href="https://fonts.googleapis.com/css2?family=Arimo:ital,wght@0,400;0,700;1,700&family=Oswald:wght@500;700&display=swap">
<style>
  :root {
    --orange: #f0701f;
    --orange-dark: #d4501a;
    --ink: #111111;
    --text: #333333;
    --white: #ffffff;
    --edge: #c9c9c9;
    --page: #ffffff;
  }
  * { margin: 0; padding: 0; box-sizing: border-box; }
  html, body { width: 1200px; height: 296px; overflow: hidden; background: var(--page); }
  body { position: relative; font-family: "Arimo", Arial, sans-serif; color: var(--text); }

  .card { position: absolute; top: 4px; width: 592px; height: 288px; overflow: hidden; }
  .card--contact { left: 4px; background: var(--white); border: 1px solid var(--edge); }
  .card--promo { left: 604px; background: var(--orange); }

  .abs { position: absolute; white-space: nowrap; }

  /* Contact side */
  .brand { left: 34px; top: 50px; display: flex; align-items: flex-end; gap: 10px; }
  .brand__mark { width: 16px; height: 16px; background: var(--orange); margin-bottom: 14px; }
  .brand__name { font-family: "Oswald", sans-serif; font-weight: 700; font-size: 50px; line-height: 1; color: var(--orange); letter-spacing: 1px; }
  .brand__sub { font-size: 14px; color: var(--text); margin-bottom: 6px; }

  .person { left: 34px; top: 188px; font-size: 14px; line-height: 18px; }
  .contacts { left: 34px; top: 230px; font-size: 13px; line-height: 14.5px; }

  .social { left: 334px; top: 50px; font-size: 15px; line-height: 18px; }
  .social__icon { display: inline-block; width: 24px; height: 24px; background: #4a67a8; vertical-align: -6px; margin-left: 8px; }
  .tagline { left: 334px; top: 124px; font-size: 15px; line-height: 18px; }
  .services { left: 334px; top: 192px; font-size: 12.5px; line-height: 15px; }

  /* Promo side */
  .promo__title { left: 60px; top: 10px; font-family: "Oswald", sans-serif; font-weight: 500; font-size: 40px; color: var(--white); letter-spacing: 1px; line-height: 1; transform: rotate(-1deg); }
  .promo__lead { left: 98px; top: 66px; font-family: "Arimo", sans-serif; font-style: italic; font-weight: 700; font-size: 14px; color: var(--white); transform: rotate(-1deg); }
  .offer { left: 36px; top: 132px; font-weight: 700; font-size: 19px; color: var(--ink); line-height: 24px; }
  .offer__value { font-size: 16px; }
  .offer__call { left: 36px; top: 200px; font-weight: 700; font-size: 21px; color: var(--ink); }
  .valid { left: 40px; top: 238px; width: 164px; height: 40px; background: var(--white); font-size: 13px; color: var(--ink); padding: 12px 0 0 12px; }
  .valid__slash { font-size: 24px; margin-left: 22px; vertical-align: -4px; }
  .perks { right: 18px; top: 228px; text-align: right; font-weight: 700; font-size: 12.5px; line-height: 18px; color: var(--ink); }
</style>
</head>
<body>

<section class="card card--contact" aria-label="Contact side">
  <div class="abs brand">
    <span class="brand__mark"></span>
    <span class="brand__name">Orlyn</span>
    <span class="brand__sub">Fitness Clubs</span>
  </div>

  <div class="abs person">
    <div>Marisol Ventura</div>
    <div>Director &amp; Head Personal Trainer</div>
  </div>

  <div class="abs contacts">
    <div>p&nbsp; 1300 555 017</div>
    <div>m&nbsp; 0400 555 293</div>
    <div>e&nbsp; marisol@orlynfitness.com.au</div>
    <div>w&nbsp; www.orlynfitness.com.au</div>
  </div>

  <div class="abs social">
    <div>Join the Orlyn Online <span class="social__icon"></span></div>
    <div>Competitions, Special Deals,</div>
    <div>Hints, Tips + More</div>
  </div>

  <div class="abs tagline">
    <div>No Judgements</div>
    <div>No Limits</div>
  </div>

  <ul class="abs services" style="list-style:none">
    <li>Personal Training</li>
    <li>Fitness Classes</li>
    <li>Boot Camps</li>
    <li>Events &amp; Adventures</li>
    <li>Corporate Fitness</li>
  </ul>
</section>

<section class="card card--promo" aria-label="Promo side">
  <svg class="abs" width="592" height="288" viewBox="0 0 592 288" aria-hidden="true" style="left:0;top:0">
    <polygon points="14,14 592,2 592,52 24,62" fill="#111111"/>
    <polygon points="78,62 470,54 462,86 86,92" fill="#d4501a"/>
  </svg>
  <div class="abs promo__title">PERSONAL TRAINING</div>
  <div class="abs promo__lead">Want to Get Fit &amp; Into Shape? Let Us Show You How.</div>

  <div class="abs offer">
    <div>FREE Initial Consult &amp; 30min 1-on-1 Session</div>
    <div class="offer__value">&nbsp;(valued $80.00)</div>
  </div>
  <div class="abs offer__call">CALL 1300 555 017 NOW TO BOOK</div>

  <div class="abs valid">Valid:<span class="valid__slash">/</span><span class="valid__slash">/</span></div>

  <div class="abs perks">
    <div>No Boring Workouts</div>
    <div>No Long Term Contracts</div>
    <div>Results Guaranteed</div>
  </div>
</section>

</body>
</html>
```